Personal Injury Lawyer Billboard

I would like a design created featuring the image of the lawyer centered in the middle of the design.
To the left of the lawyer's image it should read "INJURED?"
To the right of the lawyer's image, it should read "CALL DREW!"
Under Call Drew, include the phone number 318-555-0147.
At the bottom of the design include the lawyers information "Andrew Holloway Accident & Injury Lawyers"
PLEASE REMOVED THE BACKGROUND IMAGERY OF THE PHOTO SUBMITTED. Also, the colors for this design should match the colors shown in the logo (navy, white and relective soft gold). Please use those color combinations in ways that best stand out.

```html
<!DOCTYPE html>
<html lang="en">
<head>
<meta charset="utf-8">
<title>Injury Lawyer Billboard</title>
<link rel="stylesheet" href="https://fonts.googleapis.com/css2?family=Anton&family=Archivo+Black&family=Oswald:wght@700&display=swap">
<style>
  :root {
    --stage: #2f4a55;
    --board: #468275;
    --ink: #ffffff;
    --gold: #d9bf7a;
    --suit: #1d2652;
    --suit-deep: #141b3d;
  }
  html, body {
    margin: 0;
    width: 1200px;
    height: 999px;
    overflow: hidden;
    background: var(--stage);
  }
  .billboard {
    position: absolute;
    left: 40px;
    top: 255px;
    width: 1120px;
    height: 490px;
    background: var(--board);
    overflow: hidden;
    color: var(--ink);
  }
  .headline {
    position: absolute;
    left: 20px;
    width: 360px;
    top: 130px;
    text-align: center;
    font-family: "Anton", sans-serif;
    font-size: 104px;
    line-height: 1;
    letter-spacing: 1px;
    white-space: nowrap;
  }
  .lawyer-photo {
    position: absolute;
    left: 392px;
    top: 20px;
    width: 336px;
    height: 370px;
  }
  .call-block {
    position: absolute;
    left: 745px;
    width: 355px;
    top: 135px;
    text-align: center;
    font-family: "Oswald", sans-serif;
    font-weight: 700;
    line-height: 1;
    white-space: nowrap;
  }
  .call-name {
    font-size: 44px;
    letter-spacing: 0.5px;
  }
  .call-phone {
    margin-top: 10px;
    font-size: 54px;
    letter-spacing: -0.5px;
    color: var(--gold);
  }
  .firm-line {
    position: absolute;
    left: 0;
    right: 0;
    top: 408px;
    text-align: center;
    font-family: "Archivo Black", sans-serif;
    font-size: 30px;
    letter-spacing: 0.5px;
    white-space: nowrap;
  }
  .firm-name {
    color: var(--gold);
  }
</style>
</head>
<body>
  <main class="billboard">
    <div class="headline">Injured?</div>

    <svg class="lawyer-photo" viewBox="0 0 336 370" role="img" aria-label="Portrait photo of the lawyer in a navy suit and green tie, smiling with a raised fist, background removed">
      <defs>
        <linearGradient id="photo-fade" x1="0" y1="0" x2="0" y2="1">
          <stop offset="0" stop-color="#3c5a6a"/>
          <stop offset="0.55" stop-color="#1d2652"/>
          <stop offset="0.85" stop-color="#141b3d"/>
          <stop offset="1" stop-color="#468275"/>
        </linearGradient>
      </defs>
      <path d="M120 0 H220 V150 L300 190 Q336 210 336 260 V370 H0 V260 Q0 210 40 190 L120 150 Z" fill="url(#photo-fade)"/>
    </svg>

    <div class="call-block">
      <div class="call-name">Call Drew!</div>
      <div class="call-phone">318-555-0147</div>
    </div>

    <div class="firm-line"><span class="firm-name">Andrew Holloway</span> Accident &amp; Injury Lawyers</div>
  </main>
</body>
</html>
```